Quite like thee: needs a logo design and a business card

The business name is called: Quite like thee. It's all about fashion for everyone who needs to gain confidence and find his own style: Image Consultant, Personal Shopper. Here my Facebook fan page: https://www.facebook.com/pages/Quite-like-thee/318264907152839

I would like a smart logo & business card. The design has to be smart and long lasting. I like simplicity ("less is more"). The image needs to bring over seriousness and style. I target people from 35-65 years old. I would love to have smart warm colours like brown mole or anthracite, eventually with some berry or bordeaux red.

The copy is the following:
Quite like thee
Doreen Pavlik
Mobile: +27 72 463 08 29
eMail: pavlik.doreen@brightmailbox.net
Cape Town

Reason: I'm not in a rush.

Target Market(s)

Core target group: 35-65 years old women; wealthy; living in Cape Town
Larger target group: South Africa; eventually men too

Industry/Entity Type

Business

```html
<!DOCTYPE html>
<html lang="en">
<head>
<meta charset="utf-8">
<title>Quite like thee – Business Card</title>
<link rel="stylesheet" href="https://fonts.googleapis.com/css2?family=Jost:wght@400;500;600&display=swap">
<style>
  :root {
    --paper: #ffffff;
    --brand-orange: #c8561c;
    --ink-plum: #23123a;
    --band-brown: #4a2508;
    --band-cream: #e4d6ae;
    --vine-soft: #efe4da;
  }
  html, body {
    margin: 0;
    padding: 0;
    overflow: hidden;
    background: var(--paper);
  }
  .card {
    position: relative;
    width: 1200px;
    height: 686px;
    background: var(--paper);
    overflow: hidden;
  }
  .vine-ornament {
    position: absolute;
    left: 800px;
    top: 0;
    width: 400px;
    height: 514px;
    background: radial-gradient(ellipse at 70% 35%, var(--vine-soft) 0%, rgba(239,228,218,0.55) 45%, rgba(255,255,255,0) 75%);
  }
  .brand-name {
    position: absolute;
    left: 22px;
    top: 140px;
    margin: 0;
    font-family: "Jost", "Century Gothic", sans-serif;
    font-style: normal;
    font-weight: 400;
    font-size: 64px;
    line-height: 1;
    color: var(--brand-orange);
    white-space: nowrap;
  }
  .person-name {
    position: absolute;
    left: 22px;
    top: 242px;
    margin: 0;
    font-family: "Jost", "Century Gothic", sans-serif;
    font-weight: 600;
    font-size: 35px;
    line-height: 1;
    color: var(--ink-plum);
  }
  .roles {
    position: absolute;
    left: 22px;
    top: 291px;
    margin: 0;
    padding: 0;
    list-style: none;
    font-family: "Jost", "Century Gothic", sans-serif;
    font-weight: 400;
    font-size: 26px;
    line-height: 40px;
    color: var(--ink-plum);
  }
  .contact {
    position: absolute;
    left: 18px;
    top: 408px;
    margin: 0;
    font-family: "Jost", "Century Gothic", sans-serif;
    font-weight: 500;
    font-size: 23px;
    line-height: 29px;
    color: var(--ink-plum);
    font-style: normal;
  }
  .contact span { display: block; }
  .footer-band {
    position: absolute;
    left: 0;
    top: 578px;
    width: 1200px;
    height: 108px;
  }
</style>
</head>
<body>
<main class="card">
  <div class="vine-ornament" role="img" aria-label="Decorative brown vine with curling tendrils and heart-shaped leaves"></div>

  <h1 class="brand-name">Quite like thee</h1>
  <h2 class="person-name">Doreen Pavlik</h2>
  <ul class="roles">
    <li>Image Consultant</li>
    <li>Personal Shopper</li>
  </ul>
  <address class="contact">
    <span>Tel. No.: +27 72 463 08 29</span>
    <span>Email: pavlik.doreen@brightmailbox.net</span>
    <span>Cape Town</span>
  </address>

  <svg class="footer-band" viewBox="0 0 1200 108" aria-hidden="true">
    <rect x="0" y="3" width="1200" height="6" fill="var(--band-brown)"/>
    <rect x="0" y="10" width="1200" height="4" fill="var(--band-cream)"/>
    <rect x="0" y="17" width="1200" height="75" fill="var(--band-brown)"/>
    <rect x="0" y="94" width="1200" height="4" fill="var(--band-cream)"/>
    <rect x="0" y="100" width="1200" height="6" fill="var(--band-brown)"/>
  </svg>
</main>
</body>
</html>
```